Business Card Design

Hello,
I try and keep my business card fresh and current. So about every year i get a new one. This year I'd like something with a white background and black lettering.
Before you start - I do not want my phone number or any other description on the card other than my url and my email.

I'd like a double sided business card with
TobFarnsby.com on one side

and

Tob@TobFarnsby.com on the other side of the card

Thinking very minimalistic and modern.
I don't have a particular font i mind or how to capitalize my name or website. This card will lead people to my new website that is being designed to showcase my photography and music.

* Initial thought was the front side of the card having a grid-like pattern built out of dashes or periods, with my website sitting within the pattern and on the back side my email on a stark white background. But that might look completely lame - haha.

I'm looking forward to seeing what you come up with.

thank you,
- tob farnsby

Reason: Want to spend some more time with the designs and add a little $. thanks for all the designs - tob

Wanted to add a little $ and spend some more time with the designs.

big thanks to all who have submitted work 

- tob

Industry/Entity Type

Business

Contact Information for Business Card

www.tobfarnsby.com
tob@tobfarnsby.com

Colors
000000
ffffff

Requirements
Must have
• tobfarnsby.com
tob@tobfarnsby.com
Should not have
• phone number
any description of what i do, photography or music

```html
<!DOCTYPE html>
<html lang="en">
<head>
<meta charset="utf-8">
<title>TobFarnsby.com – Business Card</title>
<link rel="stylesheet" href="https://fonts.googleapis.com/css2?family=Lora:wght@400&display=swap">
<style>
  :root {
    --backdrop: #ffffff;
    --card: #ffffff;
    --card-edge: #d9d9d9;
    --ink: #111111;
    --petal-yellow: #f2b705;
    --petal-orange: #ef7d12;
    --petal-red: #d8261b;
    --petal-magenta: #c4145f;
    --petal-violet: #8a35c9;
    --petal-blue: #2f8fe0;
    --petal-green: #3f9a3a;
    --haze-yellow: rgba(250, 232, 150, 0.55);
    --haze-green: rgba(205, 232, 170, 0.45);
    --haze-blue: rgba(180, 210, 245, 0.45);
    --haze-pink: rgba(245, 185, 185, 0.5);
    --haze-violet: rgba(205, 185, 235, 0.45);
    --speckle: rgba(150, 160, 160, 0.12);
  }

  html, body {
    margin: 0;
    width: 1200px;
    height: 621px;
    overflow: hidden;
    background: var(--backdrop);
  }

  .sheet {
    position: relative;
    width: 1200px;
    height: 621px;
    display: flex;
    align-items: center;
    justify-content: center;
    gap: 40px;
  }

  .card {
    position: relative;
    width: 545px;
    height: 321px;
    background: var(--card);
    border: 1px solid var(--card-edge);
    overflow: hidden;
    font-family: "Lora", Georgia, serif;
    font-weight: 400;
    color: var(--ink);
  }

  .card__texture {
    position: absolute;
    inset: 0;
    background:
      radial-gradient(ellipse at 70% 20%, var(--speckle), transparent 60%),
      radial-gradient(ellipse at 20% 70%, var(--speckle), transparent 55%);
  }

  .card__fan,
  .card__haze {
    position: absolute;
  }

  /* Front side */
  .card--front .card__fan {
    left: 0;
    bottom: 0;
    width: 245px;
    height: 200px;
    border-top-right-radius: 100% 100%;
    background: linear-gradient(200deg,
      var(--petal-magenta) 0%,
      var(--petal-red) 35%,
      var(--petal-orange) 65%,
      var(--petal-yellow) 100%);
  }

  .card--front .card__haze {
    right: 0;
    top: 40px;
    width: 390px;
    height: 281px;
    border-top-left-radius: 60% 70%;
    background: linear-gradient(110deg,
      var(--haze-green) 0%,
      var(--haze-yellow) 40%,
      var(--haze-pink) 80%,
      var(--haze-violet) 100%);
    opacity: 0.7;
  }

  /* Back side */
  .card--back .card__fan {
    left: 0;
    top: 0;
    width: 250px;
    height: 230px;
    border-bottom-right-radius: 100% 100%;
    background: linear-gradient(135deg,
      var(--petal-red) 0%,
      var(--petal-orange) 20%,
      var(--petal-green) 38%,
      var(--petal-blue) 55%,
      var(--petal-violet) 75%,
      var(--petal-yellow) 100%);
  }

  .card--back .card__haze {
    right: 0;
    bottom: 0;
    width: 430px;
    height: 250px;
    border-top-left-radius: 70% 90%;
    background: linear-gradient(100deg,
      var(--haze-violet) 0%,
      var(--haze-blue) 30%,
      var(--haze-yellow) 60%,
      var(--haze-pink) 100%);
    opacity: 0.8;
  }

  .card__site,
  .card__contact {
    position: absolute;
    margin: 0;
    white-space: nowrap;
    font-weight: 400;
    line-height: 1.2;
  }

  .card--front .card__site {
    right: 40px;
    top: 100px;
    font-size: 42px;
  }

  .card--back .card__site {
    right: 24px;
    top: 172px;
    font-size: 38px;
  }

  .card__contact {
    right: 24px;
    top: 236px;
    font-size: 19px;
  }
</style>
</head>
<body>
  <main class="sheet">
    <section class="card card--front" aria-label="Business card front">
      <div class="card__texture"></div>
      <div class="card__haze" role="img" aria-label="Faint pastel flower petals fanning across the card"></div>
      <div class="card__fan" role="img" aria-label="Fan of bright yellow, orange, red and magenta flower petals"></div>
      <h1 class="card__site">TobFarnsby.com</h1>
    </section>

    <section class="card card--back" aria-label="Business card back">
      <div class="card__texture"></div>
      <div class="card__haze" role="img" aria-label="Faint pastel flower petals fanning up from the lower edge"></div>
      <div class="card__fan" role="img" aria-label="Fan of rainbow coloured flower petals in the top corner"></div>
      <p class="card__site">TobFarnsby.com</p>
      <p class="card__contact">Contact: tob@tobfarnsby.com</p>
    </section>
  </main>
</body>
</html>
```